VELMORAN RECORDS
New independent record label
VELMORAN RECORDS -
Creative Brief
www.velmoranrecords.co.uk
independent record label
we are open to your thoughts and designs.
Modern
Red used in the logo for the background colour
below header
www.plintonrecords.co.uk
www.quaystreetjournal.com
www.brindlewick.co.uk
we would like a banner in the header that slideshows the signed artists with a small text biography.

```html
<!DOCTYPE html>
<html lang="en">
<head>
<meta charset="utf-8">
<title>Velmoran Records</title>
<link href="https://fonts.googleapis.com/css2?family=Arimo:wght@400;700&family=Anton&display=swap" rel="stylesheet">
<style>
:root{
  --red:#c8141b;
  --red-deep:#6e0a0e;
  --bg-dark:#1c1c1e;
  --panel:#2b2b2e;
  --panel-edge:#444448;
  --box:#1e1e20;
  --nav-top:#5a5a5e;
  --nav-bot:#262628;
  --text:#ffffff;
  --muted:#cfcfcf;
  --accent:#e0262d;
}
*{box-sizing:border-box;margin:0;padding:0}
html,body{width:1200px;height:857px;overflow:hidden}
body{position:relative;font-family:"Arimo",Arial,sans-serif;color:var(--text);
  background:linear-gradient(180deg,var(--red) 0,var(--red) 70px,#3a0c0e 180px,var(--bg-dark) 230px,var(--bg-dark) 700px,#3a0b0d 770px,var(--red) 857px)}
.abs{position:absolute}
.brand{display:flex;align-items:center;gap:10px;font-weight:700;color:#fff;letter-spacing:1px}
.brand .dot{width:48px;height:48px;border-radius:50%;background:#3a3a3c;display:block}
.brand span{font-size:19px;line-height:1}
.login{left:756px;top:32px;display:flex;gap:6px}
.login .field{width:80px;height:14px;background:#d8d8d8;border:1px solid #888;font-size:8px;color:#666;padding:2px 4px;line-height:9px}
.login .btn{height:14px;padding:0 8px;background:#2a2a2a;font-size:8px;line-height:12px;border:1px solid #555}
.panel{left:168px;top:67px;width:864px;height:696px;background:linear-gradient(180deg,#3a3a3d,var(--panel));border:1px solid var(--panel-edge);border-radius:16px}
.nav{left:180px;top:77px;width:840px;height:55px;display:flex;align-items:center;border-radius:10px;background:linear-gradient(180deg,var(--nav-top),var(--nav-bot))}
.nav a{flex:1;text-align:center;font-size:14px;font-weight:700;color:#fff;text-decoration:none;height:42px;line-height:42px;margin:0 6px;border-radius:6px}
.nav a.active{background:linear-gradient(180deg,#7a7a7e,#3e3e42);flex:0 0 125px}
.slideshow{left:192px;top:137px;width:816px;height:247px;border-radius:6px;background:linear-gradient(180deg,#2a0406,#a10f15 45%,#5b070a);overflow:hidden}
.slideshow .artist{position:absolute;top:22px;width:100%;text-align:center;font-family:"Anton",Impact,sans-serif;font-weight:400;font-size:44px;line-height:48px;letter-spacing:1px}
.slideshow .bio{position:absolute;left:208px;top:130px;width:400px;text-align:center;font-size:12px;line-height:16px;color:#f1d6d7}
.slideshow .cta{position:absolute;left:300px;top:182px;width:252px;height:31px;border-radius:16px;background:var(--red);border:1px solid #ff5a5e;font-size:13px;line-height:29px;text-align:center}
.slideshow .dots{position:absolute;left:0;right:0;bottom:12px;display:flex;justify-content:center;gap:8px}
.slideshow .dots i{width:8px;height:8px;border-radius:50%;background:#7a1a1e;display:block}
.slideshow .dots i.on{background:#fff}
.menu{left:192px;top:398px;width:151px;height:322px;background:var(--box)}
.menu h2{margin:0 4px;height:26px;background:#f2f2f2;color:#111;font-size:14px;text-align:center;line-height:26px;border-radius:3px}
.menu ul{padding-top:6px}
.menu li{list-style:none;font-size:10px;font-weight:700;padding:0 0 0 32px;line-height:33px}
.thumbs{left:353px;top:398px;width:655px;height:111px;background:var(--box);display:flex;gap:14px;padding:8px 10px}
.thumb{width:118px}
.thumb .img{height:58px}
.thumb p{font-size:6px;color:var(--muted);margin-top:3px;line-height:8px}
.thumb p b{color:var(--accent);font-weight:400}
.news{left:353px;top:533px;width:655px;height:216px;background:var(--box);display:flex;padding:18px 12px 10px 43px}
.video .img{width:180px;height:132px;background:linear-gradient(135deg,#9fb3c5,#4f6477)}
.video p{font-size:9px;line-height:11px;color:var(--muted);width:200px;margin-top:8px}
.posts{margin-left:30px;width:380px}
.post{font-size:9px;line-height:10.5px;color:var(--muted);margin-bottom:6px}
.post b{color:var(--accent);font-weight:400;display:block}
.social{left:204px;top:770px;display:flex;gap:10px}
.social i{width:20px;height:20px;background:#7d8ea3;border-radius:3px;display:block}
.copy{left:204px;top:824px;font-size:9px}
.flinks{left:468px;top:780px;font-size:10px;font-weight:700}
.foot-brand{left:804px;top:768px}
</style>
</head>
<body>
<div class="abs brand" style="left:198px;top:10px"><i class="dot"></i><span>VELMORAN<br>RECORDS</span></div>
<div class="abs login"><div class="field">User Name</div><div class="field">Password</div><div class="btn">SIGN IN</div><div class="btn">SIGN UP</div></div>

<div class="abs panel"></div>
<nav class="abs nav"><a class="active" href="#">Home</a><a href="#">Blog</a><a href="#">News Feed</a><a href="#">Our Tour</a><a href="#">Contact Us</a></nav>

<section class="abs slideshow" role="img" aria-label="Signed artist slideshow: band silhouetted on stage under red light">
  <h1 class="artist">SIGNED ARTIST<br>THE HOLLOW PINES</h1>
  <p class="bio">A four-piece rock band from the north coast, known for loud guitars and warm harmonies.</p>
  <div class="cta">Read Full Biography</div>
  <div class="dots"><i class="on"></i><i></i><i></i><i></i></div>
</section>

<aside class="abs menu">
  <h2>Main Menu</h2>
  <ul><li>Home</li><li>Blog</li><li>Services</li><li>News Feeds</li><li>Online Store</li><li>Advance Search</li><li>Contact Us</li></ul>
</aside>

<section class="abs thumbs">
  <div class="thumb"><div class="img" role="img" aria-label="Electric guitar photo" style="background:linear-gradient(135deg,#111,#555)"></div><p><b>New release out</b><br>Fresh sounds from our latest signed artist.</p></div>
  <div class="thumb"><div class="img" role="img" aria-label="Piano keys photo" style="background:linear-gradient(180deg,#eee,#333)"></div><p><b>Studio sessions</b><br>Recording week begins in the main studio.</p></div>
  <div class="thumb"><div class="img" role="img" aria-label="Tabla drums photo" style="background:linear-gradient(135deg,#f4f4f4,#8a5a2e)"></div><p><b>World rhythms</b><br>Percussion album coming this spring.</p></div>
  <div class="thumb" style="margin-left:40px;width:70px"><div class="img" role="img" aria-label="Portrait of a signed singer" style="height:80px;background:linear-gradient(180deg,#6b6b6b,#c9b59a)"></div></div>
</section>

<section class="abs news">
  <div class="video"><div class="img" role="img" aria-label="Close-up of hands playing guitar strings"></div>
    <p><span style="color:var(--accent)">Latest video clip</span><br>Dummy text of the printing and typesetting industry. Lorem Ipsum has been the industry's standard dummy text ever since the 1500s.</p></div>
  <div class="posts">
    <div class="post"><b>Lorem Ipsum is simply - 14.05.11</b>Dummy text of the printing and typesetting industry. Lorem Ipsum has been the industry's standard dummy text ever since the 1500s. Dummy text of the printing and typesetting industry. Lorem Ipsum has been the industry's standard dummy text ever since the 1500s.</div>
    <div class="post"><b>Lorem Ipsum is simply - 12.05.11</b>Dummy text of the printing and typesetting industry. Lorem Ipsum has been the industry's standard dummy text ever since the 1500s. Dummy text of the printing and typesetting industry. Lorem Ipsum has been the industry's standard dummy text ever since the 1500s.</div>
    <div class="post"><b>Lorem Ipsum is simply - 10.05.11</b>Dummy text of the printing and typesetting industry. Lorem Ipsum has been the industry's standard dummy text ever since the 1500s. Dummy text of the printing and typesetting industry. Lorem Ipsum has been the industry's standard dummy text ever since the 1500s.</div>
  </div>
</section>

<div class="abs social"><i></i><i></i><i></i><i></i></div>
<div class="abs copy">Allright Reserved in 2011 (c)</div>
<div class="abs flinks">Home | Blog | News Feeds | Search | Music | Contact Us</div>
<div class="abs brand foot-brand"><i class="dot"></i><span>VELMORAN<br>RECORDS</span></div>
</body>
</html>
```